Keystone Habitat Australia Business Card

We need a Business Card design for our new start up company.
A unique model designed to address Australia’s growing housing affordability problem has been launched. More than half of Australians are being priced out of the property market and have resigned themselves to the fact that they may never be able to afford a home.
We have developed a unique Algorithm that allows people to get into property and reverse this trend of domination by the property investors in this country. The first of its kind model facilitates connecting people to lending facilities that do not require them to have the finance combined under the purchase contract.
Ownership is shared with a second-tier investor, made up of either family or friends if not, Keystone Habitat Australia will provide a mini property investor enabling thousands of people the opportunity to buy a home, which they otherwise thought was not possible.
Keystone Habitat Australia is addressing housing affordability for families and individuals, giving every Australian looking to buy a home the opportunity to enter the property market to live in or invest.
Under our unique model, there is no combined finance, and individuals are assessed for their percentage portion of the property only. “A unique feature of our product is it is based around the strategies used for property investment. I have developed a unique Algorithm that enables the Home buyer to purchase 60% of a property, while Keystone Habitat Australia facilitates a second-tier investor to buy the other 40%. The Algorithm locks the investor in place and enables the home buyer to stairway to full ownership. The investment is secured against real property.
Please refer to our website www.keystonehabitat.com.au for inspiration.
Also please find attached our logo.
Any further directions please ask.
Cheers Dean
Real Estate
Dean Marrow
CEO
Mobile 0400 617 290
www.keystonehabitat.com.au
Email: dean@keystonehabitat.com.au
Designer to choose colors to be used in the design.

```html
<!DOCTYPE html>
<html lang="en">
<head>
<meta charset="utf-8">
<title>Keystone Habitat Australia – Business Card</title>
<link href="https://fonts.googleapis.com/css2?family=Montserrat:wght@400;600;700&family=Open+Sans:wght@400;600&display=swap" rel="stylesheet">
<style>
  :root {
    --stage: #2b2b2d;
    --teal-light: #1cc6d8;
    --teal-dark: #0896bd;
    --brand-blue: #1a9fd0;
    --brand-green: #5aa533;
    --ink: #3b3f44;
    --paper: #fbfcfc;
    --ghost: #d3eaf0;
    --white: #ffffff;
  }
  * { box-sizing: border-box; margin: 0; padding: 0; }
  html, body { width: 1200px; height: 900px; overflow: hidden; }
  body {
    background: var(--stage);
    display: flex;
    flex-direction: column;
    align-items: center;
    justify-content: center;
    gap: 40px;
    font-family: "Open Sans", sans-serif;
  }
  .card {
    width: 700px;
    height: 400px;
    position: relative;
    overflow: hidden;
    box-shadow: 0 10px 30px rgba(0,0,0,.45);
  }

  /* Front */
  .card-front {
    background: linear-gradient(135deg, var(--teal-light) 0%, var(--teal-dark) 100%);
    color: var(--white);
    display: flex;
    flex-direction: column;
    align-items: center;
  }
  .front-brand {
    margin-top: 130px;
    display: flex;
    align-items: center;
    gap: 12px;
  }
  .brand-dot {
    width: 22px; height: 22px;
    border-radius: 50%;
    background: currentColor;
  }
  .brand-name {
    font-family: "Montserrat", sans-serif;
    font-weight: 700;
    font-size: 34px;
    letter-spacing: .2px;
  }
  .front-tagline {
    font-family: "Montserrat", sans-serif;
    font-weight: 600;
    font-size: 17px;
    margin-top: 6px;
  }
  .front-web {
    position: absolute;
    bottom: 48px;
    left: 0; right: 0;
    text-align: center;
    font-family: "Montserrat", sans-serif;
    font-size: 16px;
    letter-spacing: 6px;
  }

  /* Back */
  .card-back { background: var(--paper); }
  .back-decoration {
    position: absolute;
    right: 0; top: 0;
    width: 330px; height: 400px;
    background: linear-gradient(180deg, var(--ghost) 0%, rgba(211,234,240,.5) 100%);
    clip-path: polygon(22% 12%, 52% 0, 100% 0, 100% 100%, 0 100%, 0 60%, 22% 42%);
    opacity: .7;
  }
  .back-brand {
    position: absolute;
    left: 50px; top: 150px;
  }
  .back-brand .brand-row {
    display: flex; align-items: center; gap: 10px;
    color: var(--brand-blue);
  }
  .back-brand .brand-dot { width: 16px; height: 16px; }
  .back-brand .brand-name { font-size: 24px; }
  .back-tagline {
    font-family: "Montserrat", sans-serif;
    font-weight: 600;
    font-size: 13px;
    color: var(--brand-green);
    margin: 3px 0 0 26px;
  }
  .contact {
    position: absolute;
    left: 420px; top: 150px;
  }
  .contact-name {
    font-family: "Montserrat", sans-serif;
    font-weight: 700;
    font-size: 17px;
    color: var(--brand-blue);
    text-transform: uppercase;
  }
  .contact-role {
    font-size: 16px;
    color: var(--brand-green);
    margin-bottom: 10px;
  }
  .contact-list { list-style: none; }
  .contact-list li {
    display: flex; align-items: center; gap: 10px;
    font-size: 15px;
    color: var(--ink);
    line-height: 24px;
  }
  .contact-list svg { width: 14px; height: 14px; flex: none; }
</style>
</head>
<body>

  <section class="card card-front">
    <div class="front-brand">
      <span class="brand-dot"></span>
      <span class="brand-name">Keystone Habitat Australia</span>
    </div>
    <p class="front-tagline">Making Home Ownership Achievable</p>
    <p class="front-web">www.keystonehabitat.com.au</p>
  </section>

  <section class="card card-back">
    <div class="back-decoration" role="img" aria-label="Faint illustration of city buildings and a house roof"></div>

    <div class="back-brand">
      <div class="brand-row">
        <span class="brand-dot"></span>
        <span class="brand-name">Keystone Habitat Australia</span>
      </div>
      <p class="back-tagline">Making Home Ownership Achievable</p>
    </div>

    <div class="contact">
      <p class="contact-name">Dean Marrow</p>
      <p class="contact-role">CEO</p>
      <ul class="contact-list">
        <li>
          <svg viewBox="0 0 14 14"><rect x="3" y="1" width="8" height="12" rx="1.5" fill="none" stroke="#1a9fd0" stroke-width="1.5"/><circle cx="7" cy="11" r=".8" fill="#1a9fd0"/></svg>
          0400 617 290
        </li>
        <li>
          <svg viewBox="0 0 14 14"><rect x="1" y="3" width="12" height="8" rx="1" fill="#3b3f44"/><path d="M1.5 3.5 7 8l5.5-4.5" fill="none" stroke="#fbfcfc" stroke-width="1"/></svg>
          dean@keystonehabitat.com.au
        </li>
        <li>
          <svg viewBox="0 0 14 14"><circle cx="7" cy="7" r="6" fill="#3b3f44"/><path d="M1 7h12M7 1c-2.5 3-2.5 9 0 12M7 1c2.5 3 2.5 9 0 12" fill="none" stroke="#fbfcfc" stroke-width=".9"/></svg>
          www.keystonehabitat.com.au
        </li>
      </ul>
    </div>
  </section>

</body>
</html>
```